Boutique Recruiting Firm Needs Eye-Catching Business Cards (and potentially new logo)!

I run a recruiting company in Charleston, South Carolina. I have a ton of networking events coming up and need business cards to grab potential clients attention.

I currently have a logo but if you want to try and recreate the logo to something more modern I am open to that. If you do decide to create a new logo please submit the business card with the old logo and the new one.

Staffing Beyond the Lantern, LLC is the name of my company. I create videos to my clients and candidates which allows me to standout from my competition so I would like a business card (and possibly new logo) to do the same.

I do not specialize in any one industry of recruiting.

Industry/Entity Type

Business

```html
<!DOCTYPE html>
<html lang="en">
<head>
<meta charset="utf-8">
<title>Staffing Beyond the Lantern — Business Cards</title>
<link href="https://fonts.googleapis.com/css2?family=Open+Sans:wght@400;600&display=swap" rel="stylesheet">
<style>
  :root {
    --backdrop: #5e3f2c;
    --card: #f3f3f3;
    --ink: #1f1f1f;
    --ink-soft: #2e2e2e;
    --rule: #c9c9c9;
  }
  * { margin: 0; padding: 0; box-sizing: border-box; }
  html, body {
    width: 1200px; height: 1000px; overflow: hidden;
    background: var(--backdrop);
    font-family: "Open Sans", Arial, sans-serif;
  }
  .business-card {
    position: absolute; left: 265px; width: 666px; height: 397px;
    background: var(--card);
  }
  .business-card--first { top: 73px; }
  .business-card--second { top: 532px; }
  .perforations {
    position: absolute; left: 0; width: 100%; height: 19px;
    background: repeating-linear-gradient(90deg,
      transparent 0 10px, var(--backdrop) 10px 28px, transparent 28px 38px);
  }
  .perforations--top { top: 12px; }
  .perforations--bottom { bottom: 12px; }
  .brand-name {
    position: absolute; left: 40px; top: 148px; width: 292px;
    text-align: center;
    font-weight: 600; font-size: 27px; line-height: 1.3;
    color: var(--ink);
  }
  .divider {
    position: absolute; left: 370px; top: 85px; width: 2px; height: 228px;
    background: linear-gradient(180deg, transparent, var(--rule) 20%, var(--rule) 80%, transparent);
  }
  .contact {
    position: absolute; left: 411px; top: 98px;
    color: var(--ink-soft); font-size: 16px; line-height: 21px;
  }
  .contact__name { font-weight: 600; font-size: 22px; line-height: 28px; color: var(--ink); }
  .contact__role { margin-bottom: 22px; }
  .contact__address { margin-bottom: 13px; }
  .contact__line { display: flex; align-items: center; gap: 7px; height: 23px; }
  .contact__line svg { width: 15px; height: 15px; fill: var(--ink); flex: none; }
</style>
</head>
<body>

<section class="business-card business-card--first">
  <div class="perforations perforations--top"></div>
  <p class="brand-name">Staffing Beyond<br>the Lantern, LLC</p>
  <div class="divider"></div>
  <div class="contact">
    <p class="contact__name">Dorian Vell’</p>
    <p class="contact__role">Film Operation</p>
    <p class="contact__address">Level 12, 48 Harbor Row<br>Charleston, South Carolina</p>
    <p class="contact__line"><svg viewBox="0 0 16 16"><path d="M1 6c0-2 3-3 7-3s7 1 7 3v1h-3V6H4v1H1zM4 8h8l2 5H2z"/></svg>+ 000 000 0000</p>
    <p class="contact__line"><svg viewBox="0 0 16 16"><path d="M1 4h14v1L8 9 1 5zM1 6.5l7 4 7-4V12H1z"/></svg>info@staffingbtl.com</p>
    <p class="contact__line"><svg viewBox="0 0 16 16"><path d="M6.5 9.5l3-3M7 4.5l1.5-1.5a2.8 2.8 0 014 4L11 8.5M9 11.5L7.5 13a2.8 2.8 0 01-4-4L5 7.5" fill="none" stroke="#1f1f1f" stroke-width="1.8" stroke-linecap="round"/></svg>www.staffingbtl.com</p>
  </div>
  <div class="perforations perforations--bottom"></div>
</section>

<section class="business-card business-card--second">
  <div class="perforations perforations--top"></div>
  <p class="brand-name">Staffing Beyond<br>the Lantern, LLC</p>
  <div class="divider"></div>
  <div class="contact">
    <p class="contact__name">Dorian Vell’</p>
    <p class="contact__role">Film Operation</p>
    <p class="contact__address">Level 12, 48 Harbor Row<br>Charleston, South Carolina</p>
    <p class="contact__line"><svg viewBox="0 0 16 16"><path d="M1 6c0-2 3-3 7-3s7 1 7 3v1h-3V6H4v1H1zM4 8h8l2 5H2z"/></svg>+ 000 000 0000</p>
    <p class="contact__line"><svg viewBox="0 0 16 16"><path d="M1 4h14v1L8 9 1 5zM1 6.5l7 4 7-4V12H1z"/></svg>info@staffingbtl.com</p>
    <p class="contact__line"><svg viewBox="0 0 16 16"><path d="M6.5 9.5l3-3M7 4.5l1.5-1.5a2.8 2.8 0 014 4L11 8.5M9 11.5L7.5 13a2.8 2.8 0 01-4-4L5 7.5" fill="none" stroke="#1f1f1f" stroke-width="1.8" stroke-linecap="round"/></svg>www.staffingbtl.com</p>
  </div>
  <div class="perforations perforations--bottom"></div>
</section>

</body>
</html>
```